New Business Cards for Torvin Group

We need a new Business Card to compliment our new logo. We are a vibrant design, manufacture and install business providing recreation areas, public parks and Municipal spaces. We want business cards that are classy, modern and clean.

We have recently changed our logo, and are celebrating our 40th anniversary. We want business cards with a new modern design to reflect our status.

Target Market(s)

Customers

Contact Information for Business Card

We need all the details of our 3 offices as per the business card attached. Please disregard the old logo on the business card, the other three files show our new logo.

Requirements
Must have
• All info as per attached business card but with new logo.
Nice to have

```html
<!DOCTYPE html>
<html lang="en">
<head>
<meta charset="utf-8">
<title>Torvin Group – Business Card</title>
<link rel="stylesheet" href="https://fonts.googleapis.com/css2?family=Ubuntu:wght@400;500;700&display=swap">
<style>
  :root {
    --brand-red: #e4232b;
    --backdrop: #e8303a;
    --ink: #3d3e42;
    --rule: #b9b9bc;
    --card: #ffffff;
  }
  * { box-sizing: border-box; margin: 0; padding: 0; }
  html, body {
    width: 1200px; height: 1000px; overflow: hidden;
    background: var(--backdrop);
    font-family: "Ubuntu", sans-serif;
  }
  .card {
    position: absolute; left: 150px; top: 240px;
    width: 900px; height: 520px;
    background: var(--card);
    border-radius: 44px;
    overflow: hidden;
    box-shadow: 0 18px 40px rgba(90, 0, 0, 0.28);
  }
  .brand {
    position: absolute; left: 48px; top: 52px;
    display: flex; align-items: center; gap: 22px;
  }
  .brand-dot {
    width: 150px; height: 150px; border-radius: 50%;
    background: var(--brand-red);
  }
  .brand-name {
    font-weight: 700; font-size: 50px; line-height: 1;
    color: var(--ink); letter-spacing: 1px; text-transform: uppercase;
  }
  .divider {
    position: absolute; left: 470px; top: 32px; height: 210px;
    border-left: 2px dotted var(--rule);
  }
  .person { position: absolute; left: 505px; top: 44px; color: var(--ink); }
  .person-name { font-size: 36px; font-weight: 500; }
  .person-title {
    font-size: 15px; font-weight: 500; color: var(--brand-red);
    letter-spacing: 2.5px; text-transform: uppercase; margin-top: 2px;
  }
  .person-contact { margin-top: 26px; font-size: 23px; line-height: 1.35; }
  .offices {
    position: absolute; left: 40px; top: 272px; width: 830px;
    display: grid; grid-template-columns: 300px 265px 265px;
  }
  .office { display: flex; gap: 12px; }
  .office-icons {
    display: flex; flex-direction: column; gap: 10px; padding-top: 30px;
  }
  .office-icons svg { width: 18px; height: 18px; fill: var(--brand-red); }
  .office-title {
    font-size: 17px; font-weight: 700; color: var(--brand-red);
    text-transform: uppercase; letter-spacing: 0.5px; margin-bottom: 4px;
  }
  .office-line {
    font-size: 17px; color: var(--ink); padding: 3px 0 3px 14px;
    border-top: 1px dashed var(--rule); width: 230px;
  }
  .footer-band { position: absolute; left: 0; bottom: 0; width: 900px; height: 90px; }
  .footer-links {
    position: absolute; right: 40px; bottom: 30px;
    font-size: 18px; line-height: 24px; color: #fff; letter-spacing: 0.3px;
    white-space: nowrap;
  }
</style>
</head>
<body>
  <main class="card">
    <div class="brand">
      <div class="brand-dot"></div>
      <div class="brand-name">Torvin<br>Group</div>
    </div>

    <div class="divider"></div>

    <section class="person">
      <h1 class="person-name">Marek Dalloway</h1>
      <p class="person-title">Managing Partner</p>
      <p class="person-contact">+971 (0)50 384 7102<br>marek@torvingroup.com</p>
    </section>

    <section class="offices">
      <div class="office">
        <div class="office-icons">
          <svg viewBox="0 0 20 20" aria-label="Address"><path d="M2 6h16v11H2z M2 6l8 6 8-6" /></svg>
          <svg viewBox="0 0 20 20" aria-label="Phone"><path d="M5 2l3 4-2 2c1 2 3 4 5 5l2-2 4 3-2 3C9 17 3 11 3 4z"/></svg>
          <svg viewBox="0 0 20 20" aria-label="Fax"><path d="M3 8h14v10H3z M6 2h8v5H6z M6 11h3v2H6z M11 11h3v2h-3z"/></svg>
        </div>
        <div>
          <h2 class="office-title">Head Office</h2>
          <p class="office-line">31840 Abu Dhabi, U.A.E.</p>
          <p class="office-line">+971 (0)2 5128390</p>
          <p class="office-line">+971 (0)2 5128391</p>
        </div>
      </div>
      <div class="office">
        <div>
          <h2 class="office-title">Dubai Office</h2>
          <p class="office-line">402716 Dubai, U.A.E</p>
          <p class="office-line">+971 (0)4 3306247</p>
          <p class="office-line">+971 (0)4 3306258</p>
        </div>
      </div>
      <div class="office">
        <div>
          <h2 class="office-title">Qatar Office</h2>
          <p class="office-line">17293 Doha, Qatar</p>
          <p class="office-line">+974 44718302</p>
          <p class="office-line">+974 44735916</p>
        </div>
      </div>
    </section>

    <svg class="footer-band" viewBox="0 0 900 90" preserveAspectRatio="none" aria-hidden="true">
      <rect x="0" y="62" width="900" height="10" fill="var(--ink)"/>
      <rect x="0" y="72" width="900" height="18" fill="var(--brand-red)"/>
      <path d="M396 72 C418 72 416 22 450 22 L900 22 L900 72 Z" fill="var(--brand-red)"/>
    </svg>
    <p class="footer-links">sales@torvingroup.com | www.torvingroup.com</p>
  </main>
</body>
</html>
```